Moravelt Systems Retractable Banner

Need a design for a retractable banner (approx. 63 inches x 24 inches) Provide us with different raw file types including: ai, png. We may end up ordering a banner that is larger or smaller so please ensure the design provided can be scaled accordingly.
Key Features:
One of the two logos shown below must be displayed (your choice). We can provide other file formats for the logo if needed.
Words that have to be shown:
Your *Data Collection Problems* End Here
Our technology transforms any building into an *IoT Smart Building*
Our *Monitoring and Alerting* capabilities give you full insight and control of your devices and buildings
Please note the words within *(stars) must be accentuated in some way, please use your creative freedom.
A design that fits the look and feel of our brand, as seen in our website here: https://moraveltsys.ca/ is encouraged
Look and feel
Each slider illustrates characteristics of the customer's brand and the style your logo design should communicate.

```html
<!DOCTYPE html>
<html lang="en">
<head>
<meta charset="utf-8">
<title>Moravelt Systems Retractable Banner</title>
<link href="https://fonts.googleapis.com/css2?family=Barlow+Condensed:wght@500;600;700&family=Roboto+Condensed:wght@300;400;700&family=Exo+2:wght@700&display=swap" rel="stylesheet">
<style>
  :root {
    --stage-top: #363636;
    --stage-bottom: #7c7c7c;
    --paper: #f4f5f6;
    --ink: #1b1c1e;
    --navy: #143447;
    --teal-deep: #17596b;
    --teal: #1a93a8;
    --teal-bright: #20aabd;
    --photo-dark: #1f5a73;
    --photo-light: #9cc8d8;
    --line-gray: #d9dcdf;
    --white: #ffffff;
  }
  * { margin: 0; padding: 0; box-sizing: border-box; }
  html, body { width: 1200px; height: 2574px; overflow: hidden; }
  body {
    background: linear-gradient(180deg, var(--stage-top), var(--stage-bottom));
    position: relative;
  }
  .banner {
    position: absolute;
    left: 176px; top: 144px;
    width: 849px; height: 2230px;
    background: radial-gradient(ellipse at 30% 55%, #ffffff 0%, var(--paper) 60%, #e9ebed 100%);
    box-shadow: 0 16px 40px rgba(0,0,0,0.45);
    overflow: hidden;
  }
  .banner__art { position: absolute; left: 0; top: 0; width: 849px; height: 1000px; }
  .brand {
    position: absolute; left: 0; top: 1100px; width: 849px;
    display: flex; align-items: center; justify-content: center; gap: 26px;
  }
  .brand__dot { width: 70px; height: 70px; border-radius: 50%; background: var(--teal); }
  .brand__name {
    font-family: "Exo 2", sans-serif; font-weight: 700;
    font-size: 84px; letter-spacing: 1px; color: var(--ink);
    text-transform: uppercase; line-height: 1;
  }
  .headline {
    position: absolute; left: 0; top: 1272px; width: 849px;
    text-align: center;
    font-family: "Barlow Condensed", sans-serif; font-weight: 600;
    font-size: 92px; line-height: 86px; text-transform: uppercase; color: var(--ink);
  }
  .headline__accent { color: var(--teal); }
  .headline__accent--deep { color: var(--teal-deep); }
  .feature {
    position: absolute; left: 96px; width: 720px;
    display: flex; align-items: flex-start; gap: 50px;
  }
  .feature--building { top: 1496px; }
  .feature--monitor { top: 1710px; }
  .feature__icon { width: 144px; height: 156px; flex: none; }
  .feature__text {
    font-family: "Roboto Condensed", sans-serif; font-weight: 300;
    font-size: 45px; line-height: 56px; color: var(--ink);
    padding-top: 4px;
  }
  .feature__accent { color: var(--teal); font-weight: 700; }
  .footer {
    position: absolute; left: 0; top: 2026px; width: 849px; height: 204px;
    background: var(--navy);
    border-top: 4px solid var(--teal);
  }
  .footer__url {
    position: absolute; left: 139px; top: 1986px; width: 572px; height: 80px;
    display: flex; align-items: center; justify-content: center;
    font-family: "Barlow Condensed", sans-serif; font-weight: 600;
    font-size: 56px; color: var(--white); text-transform: uppercase;
  }
  .footer__tab { position: absolute; left: 139px; top: 1986px; width: 572px; height: 80px; }
  .footer__phone {
    position: absolute; left: 0; top: 2088px; width: 849px; text-align: center;
    font-family: "Roboto Condensed", sans-serif; font-weight: 700;
    font-size: 72px; color: var(--white); line-height: 1;
  }
</style>
</head>
<body>
  <main class="banner">
    <svg class="banner__art" viewBox="0 0 849 1000" aria-hidden="false">
      <defs>
        <linearGradient id="photo-tone" x1="0" y1="0" x2="1" y2="1">
          <stop offset="0" stop-color="var(--photo-light)"/>
          <stop offset="0.5" stop-color="#4f8fa8"/>
          <stop offset="1" stop-color="var(--photo-dark)"/>
        </linearGradient>
        <linearGradient id="band-teal" x1="0" y1="0" x2="1" y2="0">
          <stop offset="0" stop-color="var(--teal)"/>
          <stop offset="1" stop-color="var(--teal-deep)"/>
        </linearGradient>
        <linearGradient id="band-dark" x1="0" y1="0" x2="1" y2="0">
          <stop offset="0" stop-color="var(--teal-deep)"/>
          <stop offset="1" stop-color="var(--teal)"/>
        </linearGradient>
      </defs>
      <polygon role="img" aria-label="Photo of glass office towers seen from below with glowing wireless signal rings"
               points="0,0 849,0 849,820 0,700" fill="url(#photo-tone)"/>
      <polygon points="0,690 600,838 600,862 0,716" fill="var(--line-gray)"/>
      <polygon points="0,728 596,885 439,942 0,827" fill="url(#band-dark)"/>
      <polygon points="460,742 849,842 849,913 460,842" fill="url(#band-teal)"/>
      <polygon points="682,899 849,942 849,978 682,935" fill="var(--navy)"/>
    </svg>

    <div class="brand">
      <span class="brand__dot"></span>
      <span class="brand__name">Moravelt Systems</span>
    </div>

    <h1 class="headline">
      Your <span class="headline__accent">Data Collection</span><br>
      <span class="headline__accent--deep">Problems</span> End Here
    </h1>

    <section class="feature feature--building">
      <svg class="feature__icon" viewBox="0 0 144 156">
        <polygon points="72,4 138,40 138,116 72,152 6,116 6,40" fill="none" stroke="var(--teal)" stroke-width="6"/>
        <polygon points="72,16 128,46 128,110 72,140 16,110 16,46" fill="var(--teal-deep)"/>
        <g fill="none" stroke="var(--white)" stroke-width="3">
          <rect x="44" y="84" width="20" height="30"/>
          <rect x="66" y="70" width="18" height="44"/>
          <rect x="86" y="92" width="16" height="22"/>
          <path d="M60 56 a18 18 0 0 1 24 0"/>
          <path d="M54 48 a28 28 0 0 1 36 0"/>
        </g>
        <circle cx="72" cy="62" r="3" fill="var(--white)"/>
      </svg>
      <p class="feature__text">Our technology transforms<br>any building into an<br><span class="feature__accent">IoT Smart Building</span></p>
    </section>

    <section class="feature feature--monitor">
      <svg class="feature__icon" viewBox="0 0 144 156">
        <polygon points="72,4 138,40 138,116 72,152 6,116 6,40" fill="none" stroke="var(--teal)" stroke-width="6"/>
        <polygon points="72,16 128,46 128,110 72,140 16,110 16,46" fill="var(--teal-deep)"/>
        <circle cx="72" cy="76" r="32" fill="none" stroke="var(--white)" stroke-width="3"/>
        <path d="M46 76 Q72 54 98 76 Q72 98 46 76 Z" fill="none" stroke="var(--white)" stroke-width="3"/>
        <circle cx="72" cy="76" r="8" fill="var(--white)"/>
      </svg>
      <p class="feature__text">Our <span class="feature__accent">Monitoring and Alerting</span><br>capabilties give you full<br>insight and control of your<br>devices and buildings</p>
    </section>

    <div class="footer"></div>
    <svg class="footer__tab" viewBox="0 0 572 80" aria-hidden="true">
      <defs>
        <linearGradient id="tab-tone" x1="0" y1="0" x2="1" y2="0">
          <stop offset="0" stop-color="var(--teal-deep)"/>
          <stop offset="0.5" stop-color="var(--teal)"/>
          <stop offset="1" stop-color="var(--teal-deep)"/>
        </linearGradient>
      </defs>
      <polygon points="30,0 542,0 572,40 542,80 30,80 0,40" fill="url(#tab-tone)"/>
    </svg>
    <div class="footer__url">www.moraveltsys.ca</div>
    <div class="footer__phone">Call (888) 555-0142</div>
  </main>
</body>
</html>
```